Re-design web project

1.Re-design of http://www.klipzwerm.be
Logo		Ons concept 	Video referenties	Pagina delen	Promoot uw bedrijfsfilm
(Our concept)	(Video references)	(Share page)	(Promote yr company video)
Share-this buttons
Content promotion float
•	Bestel vandaag uw creatieve video en wij brengen hem vanaf 0,29 EUR onder de aandacht van potentiële klanten (Order today your creative video and we promote it online towards potential customers starting from € 0.29)
Slideshow images + content
•	Social Video = Online Video + Marketing + Social Media (Social Video = Online Video + Marketing + Social Media)
•	We verbeelden uw concept in een creatieve, aansprekende video (We visualise your concept into a creative video
•	We promoten uw video online en bereiken enkel potentiële klanten (We promote your video online and reach potential customers only)
•	Onbekende prospects worden kwalitatieve leads! (Unknown prospects are quality leads!)
Sketch + content
•	We stellen u een passend scenario voor (We propose an apropriate scenrio)
•	We visualiseren uw diensten (We visualize your services)
•	We brengen uw video onder de aandacht van potentiële klanten (We bring your video under the attention of potential customers)
•	We laten uw onderneming groeien! (We let your business grow!)
Bekijk onze video (Watch our video)
Ontvang vrijblijvend een presentatie van onze dienstverlening (Get a free presentation of our services )
Een aantal van onze video projecten (Take a look at our video projects)

Sitemap    Voorwaarden    Ons team    Contact
2. Re-design of http://www.klipzwerm.be/luxe-appartement-centrum-gent as well

```html
<!DOCTYPE html>
<html lang="nl">
<head>
<meta charset="utf-8">
<title>klipzwerm – Project 1</title>
<link rel="stylesheet" href="https://fonts.googleapis.com/css2?family=Open+Sans:wght@300;400;600;700&display=swap">
<style>
  :root {
    --dark: #434343;
    --dark-2: #3a3a3a;
    --blue: #5b93c7;
    --white: #ffffff;
    --ink: #555555;
    --ink-soft: #8c8c8c;
    --brand: #4a4a4a;
    --footer-head: #5f5f5f;
    --footer-text: #8a8a8a;
  }
  * { box-sizing: border-box; margin: 0; padding: 0; }
  html, body { width: 1200px; height: 1000px; overflow: hidden; }
  body { font-family: "Open Sans", Arial, sans-serif; background: var(--white); color: var(--ink); position: relative; }
  .abs { position: absolute; }

  .topbar { left: 0; top: 0; width: 1200px; height: 41px; background: var(--dark); }
  .social { right: 280px; top: 12px; display: flex; align-items: center; }
  .social span { width: 10px; height: 10px; background: #8c8c8c; border-radius: 2px; margin: 0 9px; }
  .social i { width: 1px; height: 20px; border-left: 1px dotted #6c6c6c; }

  .header { left: 0; top: 41px; width: 1200px; height: 57px; background: var(--white); }
  .brand { left: 283px; top: 13px; font-size: 24px; letter-spacing: -1px; color: var(--brand); font-weight: 300; display: flex; align-items: center; gap: 8px; }
  .brand .mark { width: 10px; height: 10px; background: var(--blue); }
  .nav { left: 647px; top: 0; display: flex; height: 57px; }
  .nav a { font-size: 9.5px; color: #333; text-decoration: none; padding: 0 12px; line-height: 57px; }
  .nav a.active { background: var(--blue); color: var(--white); padding: 0 14px; }

  .crumbband { left: 0; top: 98px; width: 1200px; height: 49px; background: var(--dark); }
  .crumbs { left: 283px; top: 98px; width: 646px; height: 49px; background: var(--blue); }
  .crumbs p { position: absolute; left: 10px; top: 19px; font-size: 7.5px; font-weight: 700; color: var(--white); letter-spacing: .3px; }
  .crumbs .notch { position: absolute; left: 0; bottom: 0; }
  .search { position: absolute; left: 494px; top: 14px; width: 117px; height: 19px; background: var(--white); font-size: 6.5px; color: #aaa; padding: 5px 6px; }
  .search-btn { position: absolute; left: 611px; top: 14px; width: 23px; height: 19px; background: var(--dark-2); }

  .page-title { left: 293px; top: 166px; font-size: 26px; font-weight: 300; color: #555; }
  .title-rule { left: 292px; top: 216px; width: 627px; border-top: 1px dotted #bbb; }

  .overview { left: 293px; top: 237px; width: 195px; }
  .overview h2 { font-size: 12px; font-weight: 300; color: #444; }
  .body-text { font-size: 7.4px; line-height: 13px; color: var(--ink-soft); }
  .overview .body-text { margin-top: 11px; }
  .btn-launch { left: 293px; top: 404px; width: 110px; height: 26px; background: var(--blue); color: var(--white); font-size: 12px; text-align: center; line-height: 26px; }
  .pager { left: 293px; top: 443px; display: flex; gap: 1px; }
  .pager div { width: 35px; height: 35px; background: var(--dark); display: flex; align-items: center; justify-content: center; }

  .gallery { left: 508px; top: 225px; width: 410px; height: 369px; border: 1px dotted #bbb; }
  .photo-main { position: absolute; left: 3px; top: 3px; width: 402px; height: 286px; background: linear-gradient(135deg, #8c8d84 0%, #cfd0c8 35%, #9ea039 60%, #3b3a36 100%); }
  .thumbs { position: absolute; left: 3px; top: 293px; display: flex; }
  .thumbs div { width: 100.5px; height: 72px; }
  .t1 { background: linear-gradient(160deg, #c9c9c4, #6f6b66); }
  .t2 { background: linear-gradient(160deg, #b8b8b0, #8a8b2c); }
  .t3 { background: linear-gradient(160deg, #d4cfd2, #a84a6a); }
  .t4 { background: linear-gradient(160deg, #cfd0d6, #3c55a8); }

  .col { top: 638px; width: 302px; }
  .col h3 { font-size: 10.5px; font-weight: 400; color: #444; letter-spacing: -.3px; }
  .col .body-text { margin-top: 14px; }
  .col-left { left: 293px; }
  .col-right { left: 616px; }

  .footer { left: 0; top: 752px; width: 1200px; height: 248px; background: var(--dark); }
  .newsletter { left: 283px; top: 752px; width: 646px; height: 64px; background: var(--blue); color: var(--white); }
  .newsletter h4 { position: absolute; left: 10px; top: 13px; font-size: 15px; font-weight: 400; }
  .newsletter p { position: absolute; left: 10px; top: 38px; font-size: 6.5px; font-weight: 600; }
  .newsletter .email { position: absolute; left: 440px; top: 24px; width: 130px; height: 18px; background: var(--white); font-size: 6.5px; color: #aaa; padding: 4px 6px; }
  .newsletter .subscribe { position: absolute; left: 570px; top: 24px; width: 65px; height: 18px; background: var(--dark-2); font-size: 6.5px; font-weight: 700; text-align: center; line-height: 18px; }
  .newsletter .tip { position: absolute; left: 318px; bottom: -5px; }

  .f-col h5 { font-size: 18px; font-weight: 300; color: var(--footer-head); letter-spacing: -.3px; }
  .f-col p { font-size: 7.4px; line-height: 13px; color: var(--footer-text); margin-top: 12px; }
  .f-left { left: 293px; top: 844px; width: 305px; }
  .f-right { left: 616px; top: 844px; width: 302px; }
  .contact { list-style: none; margin-top: 20px; }
  .contact li { display: flex; align-items: center; gap: 9px; font-size: 6.5px; color: #b8b8b8; height: 26px; }
  .f-input { left: 616px; top: 916px; width: 302px; height: 26px; background: var(--white); }
  .f-submit { left: 616px; top: 956px; width: 57px; height: 24px; background: var(--blue); color: var(--white); font-size: 8px; text-align: center; line-height: 24px; }
</style>
</head>
<body>
  <div class="abs topbar"></div>
  <div class="abs social">
    <span></span><i></i><span></span><i></i><span></span><i></i><span></span><i></i><span></span><i></i><span></span><i></i><span></span>
  </div>

  <header class="abs header">
    <div class="abs brand"><span class="mark"></span>klipzwerm</div>
    <nav class="abs nav">
      <a href="#">Home</a><a href="#">Features</a><a href="#">Blog</a><a href="#" class="active">Projects</a><a href="#">Contact</a>
    </nav>
  </header>

  <div class="abs crumbband"></div>
  <div class="abs crumbs">
    <p>HOME &nbsp; / &nbsp; PAGES &nbsp; / &nbsp; PROJECT - 1</p>
    <svg class="notch" width="14" height="14" viewBox="0 0 14 14"><path d="M0 0 L14 14 L0 14 Z" fill="#ffffff"/></svg>
    <div class="search">Enter search terms</div>
    <div class="search-btn">
      <svg width="23" height="19" viewBox="0 0 23 19"><circle cx="10.5" cy="8.5" r="3.5" fill="none" stroke="#fff" stroke-width="1.6"/><path d="M13 11 L15.5 13.5" stroke="#fff" stroke-width="1.8"/></svg>
    </div>
  </div>

  <h1 class="abs page-title">Project - 1</h1>
  <div class="abs title-rule"></div>

  <section class="abs overview">
    <h2>Overview</h2>
    <p class="body-text">Ruim en licht appartement in het hart van Gent, vlak bij winkels, cafés en openbaar vervoer. Grote ramen laten veel daglicht binnen in de leefruimte met open keuken en eethoek. Twee slaapkamers, een moderne badkamer en een rustige ligging aan de achterzijde maken dit pand ideaal voor wie centraal wil wonen. De parketvloer en hoge plafonds geven de ruimte extra karakter, terwijl de kelder en fietsenberging praktisch comfort bieden. Ontdek het appartement nu in onze video.</p>
  </section>
  <div class="abs btn-launch">Launch Project</div>
  <div class="abs pager">
    <div><svg width="14" height="26" viewBox="0 0 14 26"><path d="M12 1 L2 13 L12 25" fill="none" stroke="#777" stroke-width="1"/></svg></div>
    <div><svg width="20" height="20" viewBox="0 0 20 20" fill="#888"><rect x="1" y="1" width="4" height="4"/><rect x="8" y="1" width="4" height="4"/><rect x="15" y="1" width="4" height="4"/><rect x="1" y="8" width="4" height="4"/><rect x="8" y="8" width="4" height="4"/><rect x="15" y="8" width="4" height="4"/><rect x="1" y="15" width="4" height="4"/><rect x="8" y="15" width="4" height="4"/><rect x="15" y="15" width="4" height="4"/></svg></div>
    <div><svg width="14" height="26" viewBox="0 0 14 26"><path d="M2 1 L12 13 L2 25" fill="none" stroke="#777" stroke-width="1"/></svg></div>
  </div>

  <div class="abs gallery">
    <div class="photo-main" role="img" aria-label="Foto van de lichte woonkamer met eettafel, stoelen en grote ramen"></div>
    <div class="thumbs">
      <div class="t1" role="img" aria-label="Miniatuur van de woonkamer"></div>
      <div class="t2" role="img" aria-label="Miniatuur van de woonkamer met gele vloer"></div>
      <div class="t3" role="img" aria-label="Miniatuur van de woonkamer met roze vloer"></div>
      <div class="t4" role="img" aria-label="Miniatuur van de woonkamer met blauwe vloer"></div>
    </div>
  </div>

  <section class="abs col col-left">
    <h3>Koop dit luxe appartement aan de beste prijs</h3>
    <p class="body-text">Dit luxe appartement combineert een centrale ligging met een verzorgde afwerking. De parketvloer, de ruime eethoek en de grote ramen zorgen voor een warme sfeer. Bekijk de video en ontdek elke ruimte alsof u er zelf rondloopt. Neem vandaag nog contact op voor een bezoek en ontvang alle details over prijs, lasten en beschikbaarheid van het pand. Wij plannen graag een bezichtiging op een moment dat u past, ook in het weekend.</p>
  </section>
  <section class="abs col col-right">
    <h3>… Bepaal zelf hoeveel dit pand u waard is</h3>
    <p class="body-text">Wij maken een korte, aansprekende video van uw woning en brengen die online onder de aandacht van potentiële kopers. Zo bereikt u enkel mensen die echt interesse hebben. U bepaalt zelf het budget en volgt de resultaten van dag tot dag. Vraag vrijblijvend een presentatie aan en ontdek hoeveel uw pand waard is op de markt. Onze ploeg begeleidt u van het eerste idee tot de laatste kijker.</p>
  </section>

  <footer class="abs footer"></footer>
  <div class="abs newsletter">
    <h4>Sign up for our newsletter</h4>
    <p>Keep up-to-date with the latest news and updates by subscribing to our newsletter.</p>
    <div class="email">Enter your email address</div>
    <div class="subscribe">Subscribe</div>
    <svg class="tip" width="10" height="5" viewBox="0 0 10 5"><path d="M0 0 L10 0 L5 5 Z" fill="#5b93c7"/></svg>
  </div>

  <section class="abs f-col f-left">
    <h5>Bezoek het pand</h5>
    <p>We say what we do, we do what we say, and we're looking forward to prove it to you.</p>
    <ul class="contact">
      <li><svg width="10" height="14" viewBox="0 0 10 14"><path d="M5 0 C2 0 0 2.2 0 5 C0 8.5 5 14 5 14 C5 14 10 8.5 10 5 C10 2.2 8 0 5 0 Z" fill="#8a8a8a"/><circle cx="5" cy="5" r="2" fill="#434343"/></svg>12 Kouterlaan, Gent, 9000, BE</li>
      <li><svg width="10" height="14" viewBox="0 0 10 14"><rect x="0.5" y="0.5" width="9" height="13" rx="1.5" fill="none" stroke="#8a8a8a"/><rect x="2" y="2" width="6" height="8" fill="#8a8a8a"/></svg>(09) 555-0142</li>
      <li><svg width="10" height="10" viewBox="0 0 10 10"><path d="M0 4 L5 0 L10 4 V10 H0 Z" fill="#8a8a8a"/><path d="M1.5 5 L5 7.5 L8.5 5" fill="none" stroke="#434343"/></svg>office@klipzwerm.be</li>
    </ul>
  </section>
  <section class="abs f-col f-right">
    <h5>Breng uw pand onder de aandacht</h5>
    <p>Verkoopt u uw woning en wenst u deze online te promoten bij potentiële kopers? Vul dan onderstaand uw e-mailadres in.</p>
  </section>
  <div class="abs f-input"></div>
  <div class="abs f-submit">Submit</div>
</body>
</html>
```